Business Card Design for Vintage Jazz

I am a vintage jazz band leader in New York City. My groups play the music of the 1920s, 1930s and 1940s. My website is marlowpeskin.com for more info on what I do.

I am looking for a two sided business card design that has the look and feel of a really nice business card from the 1930s. I need to convey with the design that my work has that vintage kind of class and style, but also conveys that we are fun and entertaining.

Most importantly it should make a bold staement. If Hollis Varnum had a card, what would it have looked like? I want a card that I feel confident will make an impact and will let people know that my work is te the top that NYC has to offer in vintage jazz..

Note that I have only decided to avoid the "committed payment" option as I have not used this service before. Assuming that I get quality work I will select a design from those presented.

Target Market(s)

people who want to hire my band for events, media, and new fans of the band

Industry/Entity Type

Performing Art

Contact Information for Business Card

Definitely a matte finish, possibly a sort of old style of paper with that brown tint? definitely a thick card.

Requirements
Must have
• FRONT
• My name: Marlow Peskin
• What I do: Bandleader, Guitarist, Vocalist, Songwriter
• Contact Details: marlowpeskin.com marlow@marlowpeskin.com 646-555-0187
• BACK
• My Social Media Links:
• facebook.marlowpeskin.com
• twitter, instagram, linkedin: marlowpeskin
• I'm also including a photo image I would like to use. The photo's background is not needed, and to be honest isn't really desireable. Just looking to use the image of me.
Nice to have
• I'm attaching which could be used as is, omitted from the card, or altered maybe with text going around the outside of the circle or in some other way. It may need some clean up to the edges of the lettering as we only use it for the website thumbnail.
• If there's space I'd like to include the text "join our mailing list for a free song download: freesong.marlowpeskin.com" If not perhaps just "Download a Free Song at: freesong.marlowpeskin.com - something to this end.
Should not have
• anything cartoony. Don't think retro 90s's vision of the swing era, think actual swing era!
• anything modern. Got to look old school
• Try to avoid dark backgrounds. Since we often play in bars and clubs where it is dar, a d
• avoid script fonts.

```html
<!DOCTYPE html>
<html lang="en">
<head>
<meta charset="utf-8">
<title>Marlow Peskin — Business Card</title>
<link rel="stylesheet" href="https://fonts.googleapis.com/css2?family=Josefin+Sans:wght@400;600;700&display=swap">
<style>
  :root {
    --stage: #d8d6d2;
    --paper: #efe4cc;
    --paper-edge: #e3d3b1;
    --ink: #2a1e12;
    --ink-soft: #4a3a28;
    --rule: #6b5438;
    --photo-top: #b8a07c;
    --photo-mid: #6e5636;
    --photo-bottom: #2c2014;
  }
  * { box-sizing: border-box; margin: 0; padding: 0; }
  html, body {
    width: 1200px;
    height: 864px;
    overflow: hidden;
    background: var(--stage);
    font-family: "Josefin Sans", "Futura", Arial, sans-serif;
  }
  .stage { position: relative; width: 1200px; height: 864px; }
  ul { list-style: none; }

  .card {
    position: absolute;
    left: 300px;
    width: 600px;
    height: 343px;
    background: radial-gradient(ellipse at 50% 40%, var(--paper) 60%, var(--paper-edge) 100%);
    color: var(--ink);
    box-shadow: 0 6px 18px rgba(40,30,20,0.22);
  }
  .card__frame {
    position: absolute;
    inset: 12px;
    border: 2px solid var(--rule);
    pointer-events: none;
  }
  .card__frame::after {
    content: "";
    position: absolute;
    inset: 4px;
    border: 1px solid var(--rule);
  }

  /* Back side */
  .card--back { top: 66px; }
  .card--back .card__name {
    position: absolute;
    top: 110px;
    left: 0;
    width: 100%;
    text-align: center;
    font-size: 27px;
    font-weight: 700;
    letter-spacing: 1.5px;
    text-transform: uppercase;
  }
  .card--back .card__divider {
    position: absolute;
    top: 150px;
    left: 220px;
    width: 160px;
    border-top: 1px solid var(--rule);
  }
  .socials {
    position: absolute;
    top: 168px;
    left: 0;
    width: 100%;
    display: flex;
    justify-content: center;
    gap: 40px;
    font-size: 13px;
    font-weight: 600;
    color: var(--ink-soft);
  }
  .socials__col { display: flex; flex-direction: column; gap: 6px; }
  .socials__col--left { align-items: flex-end; }
  .socials__col--right { align-items: flex-start; }
  .social { display: flex; align-items: center; gap: 7px; }
  .social__mark {
    width: 10px;
    height: 10px;
    border-radius: 50%;
    background: var(--ink);
    flex: none;
  }

  /* Front side */
  .card--front { top: 452px; }
  .portrait {
    position: absolute;
    left: 62px;
    top: 30px;
    width: 178px;
    height: 182px;
    border-radius: 50%;
    border: 2px solid var(--rule);
    background: radial-gradient(ellipse at 50% 35%, var(--photo-top) 0%, var(--photo-mid) 45%, var(--photo-bottom) 100%);
  }
  .card--front .card__name {
    position: absolute;
    left: 46px;
    top: 222px;
    font-size: 24px;
    font-weight: 700;
    letter-spacing: 1px;
    text-transform: uppercase;
  }
  .brandmark {
    position: absolute;
    right: 44px;
    top: 62px;
    display: flex;
    align-items: center;
    gap: 10px;
    font-size: 18px;
    font-weight: 600;
    letter-spacing: 1px;
    text-transform: uppercase;
  }
  .brandmark__circle {
    width: 44px;
    height: 44px;
    border-radius: 50%;
    border: 2px solid var(--ink);
    flex: none;
  }
  .contact {
    position: absolute;
    right: 44px;
    top: 222px;
    text-align: right;
    font-size: 15px;
    line-height: 21px;
    color: var(--ink-soft);
  }
  .contact__item { display: flex; justify-content: flex-end; align-items: center; gap: 7px; }
  .contact__icon { width: 11px; height: 11px; flex: none; }
  .card__roles {
    position: absolute;
    right: 44px;
    top: 292px;
    font-size: 14px;
    font-weight: 700;
    letter-spacing: 0.3px;
  }
</style>
</head>
<body>
<main class="stage">

  <section class="card card--back" aria-label="Card back">
    <div class="card__frame"></div>
    <h2 class="card__name">Marlow Peskin</h2>
    <div class="card__divider"></div>
    <div class="socials">
      <ul class="socials__col socials__col--left">
        <li class="social">marlowpeskin.com <span class="social__mark"></span></li>
        <li class="social">marlowpeskin <span class="social__mark"></span></li>
      </ul>
      <ul class="socials__col socials__col--right">
        <li class="social"><span class="social__mark"></span> marlowpeskin</li>
        <li class="social"><span class="social__mark"></span> marlowpeskin</li>
      </ul>
    </div>
  </section>

  <section class="card card--front" aria-label="Card front">
    <div class="card__frame"></div>
    <div class="portrait" role="img" aria-label="Sepia portrait of the bandleader tipping a straw boater hat, in a dark blazer"></div>
    <h1 class="card__name">Marlow Peskin</h1>

    <div class="brandmark">
      <span class="brandmark__circle"></span>
      <span class="brandmark__name">Marlow Peskin</span>
    </div>

    <ul class="contact">
      <li class="contact__item">646-555-0187
        <svg class="contact__icon" viewBox="0 0 12 12" aria-hidden="true"><path d="M2.5 1 L4.5 1 L5.2 3.6 L3.9 4.6 Q5 7 7.4 8.1 L8.4 6.8 L11 7.5 L11 9.5 Q10.5 11 9 11 Q1 10 1 3 Q1 1.5 2.5 1 Z" fill="#2a1e12"/></svg>
      </li>
      <li class="contact__item">marlow@marlowpeskin.com
        <svg class="contact__icon" viewBox="0 0 12 12" aria-hidden="true"><rect x="0.5" y="2.5" width="11" height="7.5" fill="#2a1e12"/><path d="M0.8 2.8 L6 7 L11.2 2.8" stroke="#efe4cc" stroke-width="1" fill="none"/></svg>
      </li>
      <li class="contact__item">marlowpeskin.com
        <svg class="contact__icon" viewBox="0 0 12 12" aria-hidden="true"><circle cx="6" cy="6" r="5.5" fill="#2a1e12"/><path d="M0.5 6 H11.5 M6 0.5 Q2.8 6 6 11.5 M6 0.5 Q9.2 6 6 11.5" stroke="#efe4cc" stroke-width="0.8" fill="none"/></svg>
      </li>
    </ul>

    <p class="card__roles">Bandleader, Guitarist, Vocalist, Songwriter</p>
  </section>

</main>
</body>
</html>
```